Glamour By Tavi

I am a makeup artist looking for professional looking double sided business card. I would like to create a logo and incorporate a set of eyes as the periods above the name "Tavi" on the card.

front of card: Logo "Glamour by Tavi" written across diagonal (bottom left to top right)

Back of card:
1) Professional makeup artist serving New York & New Jersey (or similar to this text)
2) 917-555-0148
3) glamourbytavi@mailcove.com

Industry/Entity Type

Business

```html
<!DOCTYPE html>
<html lang="en">
<head>
<meta charset="utf-8">
<title>Glamour By Tavi – Business Card</title>
<link rel="stylesheet" href="https://fonts.googleapis.com/css2?family=Cinzel:wght@400;600&family=Open+Sans:wght@300;600;700&display=swap">
<style>
  :root {
    --page: #e6e6e6;
    --card-black: #1d1d1d;
    --card-panel: #2b2b2b;
    --logo-grey: #0c0c0c;
    --accent-red: #b3121b;
    --text-white: #f4f4f4;
    --text-soft: #9a9a9a;
  }
  * { box-sizing: border-box; margin: 0; padding: 0; }
  html, body { width: 1200px; height: 900px; overflow: hidden; }
  body {
    background: var(--page);
    font-family: "Open Sans", Arial, sans-serif;
    position: relative;
  }
  .card {
    position: absolute;
    left: 290px;
    width: 620px;
    height: 354px;
    border-radius: 18px;
    background: var(--card-black);
    overflow: hidden;
    box-shadow: 0 8px 22px rgba(0,0,0,.22);
  }
  .card--front { top: 76px; }
  .card--back { top: 470px; }

  /* Front */
  .front-logo {
    position: absolute;
    left: 0; right: 0; top: 92px;
    text-align: center;
  }
  .logo-name {
    font-family: "Open Sans", Arial, sans-serif;
    font-weight: 700;
    color: var(--logo-grey);
    letter-spacing: 2px;
    line-height: 1;
  }
  .front-logo .logo-name { font-size: 104px; }
  .logo-dot {
    display: inline-block;
    width: 14px; height: 14px;
    border-radius: 50%;
    background: var(--logo-grey);
    margin-left: 6px;
  }
  .front-tagline {
    display: inline-block;
    margin-top: 8px;
    padding-bottom: 6px;
    font-family: "Cinzel", Georgia, serif;
    font-size: 14px;
    color: var(--text-soft);
    letter-spacing: 1px;
    border-bottom: 2px solid var(--accent-red);
  }
  .front-signature {
    position: absolute;
    right: 22px; bottom: 16px;
    font-size: 10px;
    font-weight: 600;
    letter-spacing: 2px;
    color: var(--text-white);
  }

  /* Back */
  .back-panel {
    position: absolute;
    left: 0; top: 0; bottom: 0;
    width: 230px;
    background: var(--card-panel);
  }
  .eyes-art {
    position: absolute;
    inset: 0;
    background: linear-gradient(180deg, #333 0%, #2a2a2a 45%, #303030 75%, #262626 100%);
  }
  .back-logo {
    position: absolute;
    left: 24px; top: 118px;
  }
  .back-logo .logo-name { font-size: 58px; }
  .back-logo .logo-dot { width: 9px; height: 9px; }
  .back-tagline {
    display: block;
    margin-top: 4px;
    padding-bottom: 3px;
    font-family: "Cinzel", Georgia, serif;
    font-size: 8px;
    color: var(--text-soft);
    border-bottom: 1px solid var(--accent-red);
  }
  .back-content {
    position: absolute;
    left: 230px; top: 0; right: 0; bottom: 0;
    padding: 26px 22px 0 30px;
  }
  .brand-head {
    text-align: right;
    padding-right: 14px;
  }
  .brand-word {
    font-weight: 300;
    font-size: 40px;
    color: var(--text-white);
    letter-spacing: 1px;
    line-height: 1;
  }
  .brand-by {
    display: inline-block;
    font-size: 9px;
    color: var(--accent-red);
    writing-mode: vertical-rl;
    transform: rotate(180deg);
    vertical-align: bottom;
    margin-left: 2px;
  }
  .brand-rule {
    height: 2px;
    background: var(--accent-red);
    margin: 6px -22px 4px -30px;
  }
  .info-label {
    font-family: "Cinzel", Georgia, serif;
    font-size: 14px;
    color: var(--accent-red);
    letter-spacing: .5px;
    line-height: 1.15;
    display: flex;
    align-items: center;
    gap: 8px;
  }
  .info-label::before {
    content: "";
    width: 6px; height: 6px;
    border: 1px solid var(--accent-red);
    flex: none;
  }
  .info-label--plain::before { visibility: hidden; }
  .info-value {
    font-weight: 700;
    color: var(--text-white);
    padding-left: 30px;
    line-height: 1.2;
  }
  .info-value--region { font-size: 15px; }
  .info-value--phone { font-size: 20px; margin-bottom: 8px; }
  .info-value--email { font-size: 15px; }
  .info-group { margin-top: 10px; }
</style>
</head>
<body>

  <section class="card card--front" aria-label="Card front">
    <div class="front-logo">
      <div class="logo-name">Tavi<span class="logo-dot"></span></div>
      <div class="front-tagline">Professional Make Up Artist</div>
    </div>
    <div class="front-signature">GLAMOUR BY TAVI</div>
  </section>

  <section class="card card--back" aria-label="Card back">
    <div class="back-panel">
      <div class="eyes-art" role="img" aria-label="Faint illustrated eyes pattern"></div>
      <div class="back-logo">
        <div class="logo-name">Tavi<span class="logo-dot"></span></div>
        <span class="back-tagline">Professional Make Up Artist</span>
      </div>
    </div>
    <div class="back-content">
      <div class="brand-head">
        <span class="brand-word">GLAMOUR</span><span class="brand-by">by TAVI</span>
      </div>
      <div class="brand-rule"></div>
      <div class="info-label">Professional Make Up Artist</div>
      <div class="info-label info-label--plain">Serving:</div>
      <div class="info-value info-value--region">NEW YORK</div>
      <div class="info-value info-value--region">NEW JERSEY</div>
      <div class="info-group">
        <div class="info-label">Contact Number :</div>
        <div class="info-value info-value--phone">917-555-0148</div>
      </div>
      <div class="info-label">Email Address :</div>
      <div class="info-value info-value--email">GLAMOURBYTAVI@MAILCOVE.COM</div>
    </div>
  </section>

</body>
</html>
```